Etiketten-Design für Gin
Zielgruppe
Destillieren von GIN (HolgerRUM) / Zielgruppe alle die GIN Lieben :)
Aufgabenstellung
die Grunddatei besteht schon im AI Format, allerdings möchten wir gerne die Highlights in Kupfer haben wie Schrift und Holzfässer, gerne auch eigene Bilder entwerfen. Lediglich das HolgerRUM Logo (Kopf) sollte erhalten bleiben. Bitte die Datei so anlegen das die Highlights in Kupfer gedruckt (Siebdruck) werden können. Transparentes Etikett wäre super! Bei Fragen einfach melden :)

```html
<!DOCTYPE html>
<html lang="de">
<head>
<meta charset="utf-8">
<title>Holger – Barrel Aged GIN Etikett</title>
<link rel="stylesheet" href="https://fonts.googleapis.com/css2?family=Cormorant+Garamond:wght@500;600&display=swap">
<style>
  :root {
    --backdrop: #e9eef0;
    --glass: #cfe0e2;
    --texture-grey: #6f6f72;
    --portrait-light: #f6f6fb;
    --portrait-shade: #c9c8de;
    --copper: #c98f4a;
    --label-white: #ffffff;
  }
  html, body {
    margin: 0;
    width: 1200px;
    height: 1200px;
    overflow: hidden;
    background: var(--backdrop);
  }
  .canvas {
    position: relative;
    width: 1200px;
    height: 1200px;
  }
  .label {
    position: absolute;
    left: 150px;
    top: 150px;
    width: 900px;
    height: 900px;
    background: var(--glass);
    font-family: "Cormorant Garamond", Georgia, serif;
  }
  .label__texture {
    position: absolute;
    inset: 0;
    background:
      radial-gradient(ellipse 62% 58% at 50% 52%, rgba(111,111,114,0) 55%, rgba(111,111,114,0.55) 85%, rgba(111,111,114,0.85) 100%),
      linear-gradient(180deg, rgba(111,111,114,0.75) 0%, rgba(111,111,114,0.15) 35%, rgba(111,111,114,0.1) 70%, rgba(111,111,114,0.5) 100%);
  }
  .label__portrait {
    position: absolute;
    left: 220px;
    top: 55px;
    width: 500px;
    height: 540px;
    border-radius: 46% 46% 42% 42%;
    background: radial-gradient(ellipse at 45% 45%, var(--portrait-light) 45%, var(--portrait-shade) 100%);
  }
  .label__name {
    position: absolute;
    left: 0;
    right: 0;
    top: 600px;
    margin: 0;
    text-align: center;
    font-weight: 600;
    font-size: 120px;
    line-height: 1;
    color: var(--copper);
  }
  .label__product {
    position: absolute;
    left: 0;
    right: 0;
    top: 745px;
    margin: 0;
    text-align: center;
    font-weight: 500;
    font-size: 58px;
    line-height: 1;
    color: var(--label-white);
  }
  .label__facts {
    position: absolute;
    left: 108px;
    right: 110px;
    top: 842px;
    display: flex;
    justify-content: space-between;
    font-weight: 500;
    font-size: 30px;
    line-height: 1;
    color: var(--copper);
  }
</style>
</head>
<body>
  <main class="canvas">
    <section class="label">
      <div class="label__texture" role="img" aria-label="Gerasterte graue Drucktextur als Rahmen des transparenten Etiketts"></div>
      <div class="label__portrait" role="img" aria-label="Gezeichnetes Porträt des Brenners in Weiß und zartem Lila"></div>
      <h1 class="label__name">Holger</h1>
      <p class="label__product">Barrel Aged GIN</p>
      <div class="label__facts">
        <span class="label__abv">45% vol</span>
        <span class="label__volume">0,5L</span>
      </div>
    </section>
  </main>
</body>
</html>
```